verdant terraces simple classy business card design

my name is owen harlow and I run a gardening business aimed at high class verdant terraces. the business name is verdant terraces and our logo was designed on pixel forum .My clientel are anything from residential homes to businesses. I take pride in my work and know that I offer a service like no other in my area.
The business card will be used to represent my business and I want it to be not only rememberable, but simplistic and modern. Eye catching too. Of course I would like it relatable to gardening and appealing to the correct clientel - those being garden enthusiasts, prestigious homes and businesses that are after top of the line gardening services like no other on the market.
I am not a typical lawn mowing business so I don't want a typical card design that represents that. The gardens I work with are generally million dollar properties with owners who are very garden proud looking for upkeep and guidance from me along with sometimes whole new garden designs. I want the business cards to show to my clients that I take pride, as they do, in their garden. And I want them to know from my card that I am a professional, qualified horticulturist offering them a top of the line service for life. I want them to refer my business on. I want them to look at my business card and see class and professionalism in a modern unique bold way.
The card should be simple with the possibility of the logo on the front being embossed/debossed and my details on the back the card should have a organic garden feel it's very important to me that it is absolutely perfect
I am also very open to ideas and suggestions so look forward to seeing the designs. the business logo has been supplied with this project and I want the card to be double sided

Contact info is
Owen Harlow - Managing Director / Horticulturist
Phone : 0481 526 704
Email: owenharlow@verdantterraces.com.au

Target Market(s)

high class gardens residential and commercial

Industry/Entity Type

Gardener

Contact Information for Business Card

Contact info is
Phone : 0481 526 704

PLEASE MAKE CARD DOUBLE SIDED

Requirements
Must have
• organic simple classy modern feel
• must flow with the current logo that has been supplied with this project
• Double sided
• Must explain in a simple way that I deal with high end gardens and I'm a qualified horticulturist
Nice to have
• embossed debossed logo
Should not have
• shouldn't be to busy or cheap looking

```html
<!DOCTYPE html>
<html lang="en">
<head>
<meta charset="utf-8">
<title>Verdant Terraces – Business Card</title>
<link href="https://fonts.googleapis.com/css2?family=Lato:ital,wght@0,300;0,400;0,700;1,700&display=swap" rel="stylesheet">
<style>
  :root {
    --backdrop: #ecebe8;
    --card-black: #1c1c1c;
    --card-white: #f7f7f5;
    --leaf-green: #5cb04a;
    --leaf-green-soft: #7fcb6a;
    --ink: #2b2b2b;
    --ink-muted: #555555;
    --rule: #3a3a3a;
    --deboss: #262626;
  }
  * { box-sizing: border-box; margin: 0; padding: 0; }
  html, body {
    width: 1200px; height: 775px; overflow: hidden;
    background: var(--backdrop);
    font-family: "Lato", sans-serif;
  }
  .sheet {
    width: 1200px; height: 775px;
    display: flex; align-items: center; justify-content: center; gap: 60px;
  }
  .card {
    width: 530px; height: 303px;
    position: relative; overflow: hidden;
    box-shadow: 0 10px 30px rgba(0,0,0,0.18);
  }

  /* Front */
  .card-front { background: var(--card-black); }
  .front-emblem {
    position: absolute; left: -60px; top: -70px;
    width: 300px; height: 300px; border-radius: 50%;
    background: radial-gradient(circle at 45% 45%, #2c2c2c 0%, var(--deboss) 60%, var(--card-black) 100%);
  }
  .front-brand {
    position: absolute; right: 44px; bottom: 58px;
    display: flex; align-items: center; gap: 16px;
  }
  .front-brand .brand-name {
    font-size: 34px; font-weight: 700; letter-spacing: 3px;
    text-transform: uppercase; color: var(--leaf-green-soft);
    line-height: 1.05; text-align: right;
  }
  .front-brand .brand-dot {
    width: 62px; height: 62px; border-radius: 50%;
    background: var(--leaf-green-soft);
  }

  /* Back */
  .card-back { background: var(--card-white); }
  .back-brand {
    position: absolute; left: 40px; top: 42px;
    display: flex; align-items: center; gap: 12px;
  }
  .back-brand .brand-name {
    font-size: 24px; font-weight: 700; letter-spacing: 2px;
    text-transform: uppercase; color: var(--leaf-green);
    line-height: 1.1;
  }
  .back-brand .brand-dot {
    width: 40px; height: 40px; border-radius: 50%;
    background: var(--leaf-green);
  }
  .divider {
    position: absolute; left: 40px; top: 138px;
    width: 300px; height: 1px; background: var(--rule);
  }
  .contact {
    position: absolute; left: 40px; top: 150px;
  }
  .contact .person {
    font-size: 22px; font-weight: 300; color: var(--ink);
  }
  .contact .role {
    margin-top: 6px;
    font-size: 15px; font-weight: 700; font-style: italic;
    color: var(--leaf-green);
  }
  .contact .line {
    margin-top: 12px;
    display: flex; align-items: center; gap: 10px;
    font-size: 14px; font-weight: 400; color: var(--ink-muted);
  }
  .contact .line + .line { margin-top: 6px; }
  .contact .line svg { width: 14px; height: 14px; flex: none; }
</style>
</head>
<body>
<main class="sheet">
  <section class="card card-front" aria-label="Card front">
    <div class="front-emblem" role="img" aria-label="Debossed emblem area"></div>
    <div class="front-brand">
      <span class="brand-name">Verdant<br>Terraces</span>
      <span class="brand-dot"></span>
    </div>
  </section>

  <section class="card card-back" aria-label="Card back">
    <div class="back-brand">
      <span class="brand-name">Verdant<br>Terraces</span>
      <span class="brand-dot"></span>
    </div>
    <div class="divider"></div>
    <div class="contact">
      <p class="person">Owen Harlow</p>
      <p class="role">Managing Director / Horticulturist</p>
      <p class="line">
        <svg viewBox="0 0 14 14" aria-hidden="true">
          <rect width="14" height="14" rx="2" fill="#5cb04a"/>
          <path d="M4.2 3.2 L5.8 3.2 L6.4 5.2 L5.4 6 Q6.2 7.8 8 8.6 L8.8 7.6 L10.8 8.2 L10.8 9.8 Q10.8 10.8 9.8 10.8 Q3.2 10.4 3.2 4.2 Q3.2 3.2 4.2 3.2 Z" fill="#fff"/>
        </svg>
        0481 526 704
      </p>
      <p class="line">
        <svg viewBox="0 0 14 14" aria-hidden="true">
          <rect width="14" height="14" rx="2" fill="#5cb04a"/>
          <rect x="2.5" y="4" width="9" height="6.5" fill="none" stroke="#fff" stroke-width="1"/>
          <path d="M2.5 4 L7 7.8 L11.5 4" fill="none" stroke="#fff" stroke-width="1"/>
        </svg>
        owenharlow@verdantterraces.com.au
      </p>
    </div>
  </section>
</main>
</body>
</html>
```